KVAP Property Flyer - For Support Coordinators

Revamping our current brochures and social media posts for our properties. We need a clearer, simpler design that would be designed for Support Coordinators. Attached is our current brochure for reference.

Key details to highlight would include:
- Type of property: Studio Apartments with Psychosocial Disability Support located in Inner West
- Accommodation features
- Services

Our logo is also attached, please make the brochure with similar branding colours and fonts.

Designs look the same

Sick

Font styles to use
Sans Serif
Other font styles liked:
• Montserrat Light and Montserrat Semi Bold

Colors
0054AA
0677BA
7BADD7
CADEEF
E8F1F8

Requirements
Nice to have
• Please refer to this style guide: https://slides.trovelmark.com/deck/8TkwPzLmRd5VbQx2NcYh4GfJs7AeUo9WiKnBrMp3tZq/view?mode=shared

```html
<!DOCTYPE html>
<html lang="en">
<head>
<meta charset="utf-8">
<title>KVAP Property Flyer – Kindred Living Care</title>
<link rel="stylesheet" href="https://fonts.googleapis.com/css2?family=Montserrat:wght@300;400;500;600;700&display=swap">
<style>
  :root {
    --blue-deep: #0054AA;
    --blue: #0677BA;
    --blue-band: #2E8BC4;
    --blue-soft: #7BADD7;
    --blue-pale: #CADEEF;
    --blue-mist: #E8F1F8;
    --panel: #555759;
    --panel-dark: #4A4B4D;
    --ink: #3C3C3C;
    --text-light: #FFFFFF;
    --backdrop: #EEF2F6;
  }
  * { box-sizing: border-box; margin: 0; padding: 0; }
  html, body {
    width: 885px; height: 1200px; overflow: hidden;
    background: var(--backdrop);
    font-family: "Montserrat", sans-serif;
    color: var(--ink);
  }
  .spread {
    position: relative; width: 885px; height: 1200px;
    display: flex; justify-content: center; align-items: center; gap: 18px;
  }
  .page {
    position: relative; width: 420px; height: 590px;
    background: #fff; overflow: hidden;
    box-shadow: 0 14px 28px rgba(40, 55, 75, .18);
  }
  .header { position: absolute; left: 0; top: 0; width: 100%; height: 94px; }
  .header--blue { background: var(--blue-band); }
  .brand {
    position: absolute; left: 18px; top: 58px;
    display: flex; align-items: center; gap: 7px;
    font-weight: 400; font-size: 11.5px; letter-spacing: .4px;
    color: var(--blue);
  }
  .brand__dot { width: 10px; height: 10px; border-radius: 50%; background: var(--blue-soft); }
  .header--blue .brand { color: var(--text-light); }
  .header--blue .brand__dot { background: var(--blue-pale); }
  .contact {
    position: absolute; left: 188px; top: 40px;
    font-size: 7.6px; font-weight: 300; line-height: 1.35;
    color: var(--ink);
  }
  .header--blue .contact { color: var(--text-light); }
  .contact__row { display: flex; align-items: flex-start; gap: 6px; }
  .contact__row--lines { margin-top: 14px; gap: 14px; }
  .contact__item { display: flex; align-items: center; gap: 6px; }
  .contact__phone { font-weight: 600; }
  .contact svg { flex: none; }
  .photo { position: absolute; display: block; }
  .photo--hero {
    left: 0; top: 94px; width: 420px; height: 172px;
    background: linear-gradient(120deg, #E9E4DC 0%, #BFB3A3 35%, #7E7466 65%, #C8C4BC 100%);
  }
  .title-band {
    position: absolute; left: 11px; top: 232px; width: 399px; height: 46px;
    background: var(--blue-band); color: var(--text-light);
    text-align: center; padding-top: 7px;
    font-size: 12.5px; line-height: 1.35;
  }
  .title-band strong { font-weight: 600; }
  .title-band span { font-weight: 300; }
  .gallery { position: absolute; left: 11px; top: 293px; width: 399px; display: flex; justify-content: space-between; }
  .gallery__item { width: 120px; }
  .gallery__photo { width: 120px; height: 117px; }
  .photo--lounge { background: linear-gradient(160deg, #D8D6D2, #8E8A84 60%, #3E3D3B); }
  .photo--kitchen { background: linear-gradient(180deg, #F2F2F0, #D9D9D6 55%, #3A3C3E); }
  .photo--living { background: linear-gradient(170deg, #C9D3DB, #EDEBE6 55%, #A29888); }
  .gallery__caption {
    margin-top: 5px; font-size: 5.6px; font-weight: 600; line-height: 1.3;
    color: var(--blue);
  }
  .gallery__rule { margin-top: 4px; width: 16px; height: 1.5px; background: var(--blue); }
  .panel {
    position: absolute; left: 11px; top: 443px; width: 399px; height: 141px;
    background: var(--panel); color: var(--text-light);
  }
  .panel__title {
    height: 20px; background: var(--panel-dark);
    text-align: center; font-size: 8.6px; font-weight: 600;
    letter-spacing: 3.6px; line-height: 20px;
  }
  .panel__cols { display: flex; padding: 10px 4px 0; height: 121px; }
  .panel__col {
    flex: 1; text-align: center; padding: 0 6px;
    border-left: 1px solid rgba(255,255,255,.45);
    margin-bottom: 14px;
  }
  .panel__col:first-child { border-left: 0; }
  .panel__icon { height: 22px; display: flex; justify-content: center; align-items: center; }
  .panel__head { margin-top: 6px; font-size: 6.2px; font-weight: 600; color: var(--blue-soft); }
  .panel__text { margin-top: 2px; font-size: 5.1px; font-weight: 300; line-height: 1.45; }
  .about { position: absolute; left: 24px; top: 116px; width: 372px; text-align: center; }
  .about__title { font-size: 16px; font-weight: 600; color: var(--blue); }
  .about__text { margin-top: 10px; font-size: 5.6px; font-weight: 300; line-height: 1.5; }
  .about__text p + p { margin-top: 7px; }
  .photo--park {
    left: 0; top: 266px; width: 420px; height: 171px;
    background: linear-gradient(110deg, #6E7A5C 0%, #9AA58A 40%, #C4C7B8 65%, #7D8A6A 100%);
  }
  .coord {
    position: absolute; left: 24px; top: 298px; width: 178px; height: 96px;
    background: rgba(60, 62, 58, .55); color: var(--text-light);
    text-align: center; padding: 6px 8px;
    font-size: 5.1px; font-weight: 300; line-height: 1.5;
  }
  .coord__head { font-size: 6px; font-weight: 600; color: var(--blue-pale); margin-bottom: 1px; }
  .coord p + p { margin-top: 5px; }
</style>
</head>
<body>
<main class="spread">

  <article class="page page--front">
    <header class="header">
      <div class="brand"><span class="brand__dot"></span>KINDRED LIVING CARE</div>
      <div class="contact">
        <div class="contact__row">
          <svg width="7" height="9" viewBox="0 0 7 9"><path d="M3.5 0A3.2 3.2 0 0 0 .3 3.2C.3 5.5 3.5 9 3.5 9s3.2-3.5 3.2-5.8A3.2 3.2 0 0 0 3.5 0zm0 4.4a1.2 1.2 0 1 1 0-2.4 1.2 1.2 0 0 1 0 2.4z" fill="var(--blue)"/></svg>
          <div>Suite 4C, Level 2,<br>18 Harlow Lane, Marrickville NSW 2204</div>
        </div>
        <div class="contact__row contact__row--lines">
          <span class="contact__item contact__phone">
            <svg width="8" height="8" viewBox="0 0 8 8"><path d="M1.6.3l1.2 1.5-.6 1a4.6 4.6 0 0 0 2.9 2.9l1-.6 1.5 1.2-.7 1.4C3.7 7.6.4 4.3.3 1z" fill="var(--blue)"/></svg>
            1300 555 018</span>
          <span class="contact__item">
            <svg width="8" height="6" viewBox="0 0 8 6"><rect width="8" height="6" rx=".6" fill="var(--blue)"/><path d="M.5.6L4 3.4 7.5.6" stroke="#fff" stroke-width=".7" fill="none"/></svg>
            hello@kindredlivingcare.com.au</span>
        </div>
      </div>
    </header>

    <div class="photo photo--hero" role="img" aria-label="Photo of residents and a support worker in a wheelchair chatting around a shared dining table"></div>
    <h1 class="title-band"><strong>Studio Apartments</strong> <span>with</span> <strong>Psychosocial Disability</strong><br><span>Support located in Inner West</span></h1>

    <section class="gallery">
      <figure class="gallery__item">
        <div class="gallery__photo photo--lounge" role="img" aria-label="Photo of a lounge room with a dark leather sofa and timber coffee table"></div>
        <figcaption class="gallery__caption">Western Sydney<br>SDA &amp; SIL</figcaption>
        <div class="gallery__rule"></div>
      </figure>
      <figure class="gallery__item">
        <div class="gallery__photo photo--kitchen" role="img" aria-label="Photo of a bright studio kitchen with dark cabinetry and a large window"></div>
        <figcaption class="gallery__caption">Inner West Supported<br>Independent Living</figcaption>
        <div class="gallery__rule"></div>
      </figure>
      <figure class="gallery__item">
        <div class="gallery__photo photo--living" role="img" aria-label="Photo of an open plan living and dining area with balcony views"></div>
        <figcaption class="gallery__caption">Wollongong - Supported Independent<br>Living Apartments</figcaption>
        <div class="gallery__rule"></div>
      </figure>
    </section>

    <section class="panel">
      <h2 class="panel__title">TRANSPORTATION FEATURES</h2>
      <div class="panel__cols">
        <div class="panel__col">
          <div class="panel__icon"><svg width="18" height="18" viewBox="0 0 18 18" stroke="#fff" stroke-width="1.1" fill="none" stroke-linecap="round"><path d="M9 1v16M2 5l14 8M2 13l14-8M7 2.5l2 2 2-2M7 15.5l2-2 2 2"/></svg></div>
          <div class="panel__head">Air Conditioning</div>
          <div class="panel__text">All our vehicles will be temperature and humidity moderated for your comfort.</div>
        </div>
        <div class="panel__col">
          <div class="panel__icon"><svg width="18" height="20" viewBox="0 0 18 20" stroke="#fff" stroke-width="1.1" fill="none" stroke-linejoin="round"><path d="M9 1l7 3v5c0 5-3.2 8.2-7 10-3.8-1.8-7-5-7-10V4z"/><path d="M5.5 10l2.5 2.5 4.5-5"/></svg></div>
          <div class="panel__head">Safety Features</div>
          <div class="panel__text">Our vehicles come equipped with suitable seat belts and airbags for any special seating/wheelchair required.</div>
        </div>
        <div class="panel__col">
          <div class="panel__icon"><svg width="18" height="20" viewBox="0 0 18 20" stroke="#fff" stroke-width="1.2" fill="none" stroke-linecap="round"><circle cx="7" cy="2.5" r="1.6" fill="#fff" stroke="none"/><path d="M7 5.5v6h5l2.5 5"/><path d="M7 8h4"/><path d="M5 9.2a5 5 0 1 0 6.8 6.3"/></svg></div>
          <div class="panel__head">Accessibility</div>
          <div class="panel__text">Our vehicles are wheelchair accessible with lift mechanisms installed to make boarding an ease.</div>
        </div>
        <div class="panel__col">
          <div class="panel__icon"><svg width="16" height="20" viewBox="0 0 16 20" stroke="#fff" stroke-width="1.1" fill="none"><path d="M3 5h10l-1-3H4z"/><circle cx="8" cy="8.5" r="3"/><path d="M2 19v-3a6 6 0 0 1 12 0v3z"/></svg></div>
          <div class="panel__head">Trusted Drivers</div>
          <div class="panel__text">Be confident you will arrive at your community event, the shops, or other destination!</div>
        </div>
      </div>
    </section>
  </article>

  <article class="page page--back">
    <header class="header header--blue">
      <div class="brand"><span class="brand__dot"></span>KINDRED LIVING CARE</div>
      <div class="contact">
        <div class="contact__row">
          <svg width="7" height="9" viewBox="0 0 7 9"><path d="M3.5 0A3.2 3.2 0 0 0 .3 3.2C.3 5.5 3.5 9 3.5 9s3.2-3.5 3.2-5.8A3.2 3.2 0 0 0 3.5 0zm0 4.4a1.2 1.2 0 1 1 0-2.4 1.2 1.2 0 0 1 0 2.4z" fill="#fff"/></svg>
          <div>Suite 4C, Level 2,<br>18 Harlow Lane, Marrickville NSW 2204</div>
        </div>
        <div class="contact__row contact__row--lines">
          <span class="contact__item contact__phone">
            <svg width="8" height="8" viewBox="0 0 8 8"><path d="M1.6.3l1.2 1.5-.6 1a4.6 4.6 0 0 0 2.9 2.9l1-.6 1.5 1.2-.7 1.4C3.7 7.6.4 4.3.3 1z" fill="#fff"/></svg>
            1300 555 018</span>
          <span class="contact__item">
            <svg width="8" height="6" viewBox="0 0 8 6"><rect width="8" height="6" rx=".6" fill="#fff"/><path d="M.5.6L4 3.4 7.5.6" stroke="var(--blue-band)" stroke-width=".7" fill="none"/></svg>
            hello@kindredlivingcare.com.au</span>
        </div>
      </div>
    </header>

    <section class="about">
      <h1 class="about__title">About KVAP</h1>
      <div class="about__text">
        <p>KVAP stands for Kinship Vital Assistance Program.<br>It is a Government initiative that provide billions of dollars in funding directly to individuals who have a substantial disability that will impact how they complete daily activities either temporarily or for the rest of their lives.</p>
        <p>The KVAA (Kinship Vital Assistance Authority) are the body that make the decision about who is eligible to become a KVAP participant and how much funding they will receive.</p>
        <p>It is not a welfare program but an Insurance Scheme to ensure that people with disabilities can have peace and security in life. Being able to live out their hopes and dreams is important for anyone and KVAP funding allows for a better quality of life for each participant.</p>
      </div>
    </section>

    <div class="photo photo--park" role="img" aria-label="Photo of a carer pushing a person in a wheelchair along a leafy park path"></div>
    <aside class="coord">
      <div class="coord__head">Local Area Coordinators (LAC)</div>
      <p>The LAC or Local Area Coordinators are the representative of the KVAP in the community and they are able to work with people to develop a KVAP submission or plan and provide support to help participants to achieve their goals.</p>
      <p>Your LAC will help you go through the submission process and direct you in a management plan and expected implementation.</p>
    </aside>

    <section class="panel">
      <h2 class="panel__title">WHERE TO BEGIN?</h2>
      <div class="panel__cols">
        <div class="panel__col">
          <div class="panel__icon"><svg width="16" height="20" viewBox="0 0 16 20" stroke="#fff" stroke-width="1.1" fill="none"><rect x="1" y="2" width="14" height="17" rx="1"/><path d="M5 1h6v3H5zM4 8h8M4 11h8M4 14h5"/></svg></div>
          <div class="panel__head">Creating your Plan</div>
          <div class="panel__text">Your plan will be developed with you by KVAP or LAC and submitted for approval. Your approval will be uploaded to the CarePortal which part of the GovLink website.</div>
        </div>
        <div class="panel__col">
          <div class="panel__icon"><svg width="16" height="20" viewBox="0 0 16 20" stroke="#fff" stroke-width="1.1" fill="none" stroke-linejoin="round"><path d="M6 9V2.5a1.3 1.3 0 0 1 2.6 0V9l4.2.8a1.6 1.6 0 0 1 1.3 1.8L13.4 17H6.5L3 12.5a1.3 1.3 0 0 1 2-1.6L6 12"/></svg></div>
          <div class="panel__head">Using Your Plan</div>
          <div class="panel__text">Using your plan means that you can self manage your own services using the CarePortal looking after your funding and arranging and paying for your service needs. If this is too challenging you can use the help of a registered service provider like Kindred Living Care to assist you with managing your plan and implementing it.</div>
        </div>
        <div class="panel__col">
          <div class="panel__icon"><svg width="16" height="20" viewBox="0 0 16 20" stroke="#fff" stroke-width="1.1" fill="none"><rect x="1" y="2" width="14" height="17" rx="1"/><path d="M5 1h6v3H5zM4 9l1.2 1.2L7.5 8M9 9.5h3M4 14l1.2 1.2L7.5 13M9 14.5h3"/></svg></div>
          <div class="panel__head">Reviewing Your Plan</div>
          <div class="panel__text">Over time your plan might change and so there is usually a yearly review of how the plan is working and if it continues to suit your needs. If it is found to be inadequate your LAC will help you draw up a new plan.</div>
        </div>
      </div>
    </section>
  </article>

</main>
</body>
</html>
```